Flyer promoting Veltrane's workshops and credentials

We run Training workshops for the data analyst community. We'd like a flyer to sell our services using a style and colour scheme consistent with our website www.veltranepartners.co.uk . I've attached some background info and some existing e-brochures for different workshops to give a flavour for content (but these are poorly designed and we don't want a similar design!!). There's also an overview document which gives more direction. The flyer will be sent with an accompanying letter to Learning & Development decision makers as well as Anlaytical team managers. It's purpose would be to generate enquiries and bookings for primarliy our flagship workshop 'Turning Figures Into Real Gains'.

Target Market(s)

Learning and Development senior managers
Analytical team managers

Industry/Entity Type

Training

Other font styles liked:
• Similar to website for consistency

Requirements
Must have
• Good copy! Slick design more in line with European (UK) style advertising rather than US.
Nice to have
• Some humour,
Should not have
• should not be as boring and non-sales based as the website!! Website is not a great example!

```html
<!DOCTYPE html>
<html lang="en">
<head>
<meta charset="utf-8">
<title>Veltrane Workshops for Data Analysts</title>
<link rel="stylesheet" href="https://fonts.googleapis.com/css2?family=Oswald:wght@500;600&family=Open+Sans:ital,wght@0,400;0,600;0,700;1,400;1,700&display=swap">
<style>
  :root {
    --navy: #0d2a4f;
    --blue: #1c5fa8;
    --blue-mid: #2a76c4;
    --orange: #f47b20;
    --ink: #2d3440;
    --muted: #5a6270;
    --white: #ffffff;
  }
  * { margin: 0; padding: 0; box-sizing: border-box; }
  html, body { width: 835px; height: 1200px; overflow: hidden; background: var(--white); }
  body { font-family: "Open Sans", Arial, sans-serif; color: var(--ink); }
  .flyer { position: relative; width: 835px; height: 1200px; overflow: hidden; background: var(--white); }

  .hero { position: absolute; left: 0; top: 0; width: 835px; height: 480px; }
  .hero-photo { position: absolute; inset: 0; background: radial-gradient(ellipse at 62% 40%, #3d7fc4 0%, #1a4c86 40%, var(--navy) 80%); }
  .swoosh { position: absolute; left: 0; top: 0; width: 835px; height: 480px; }

  .brand { position: absolute; left: 44px; top: 44px; display: flex; align-items: center; gap: 10px; }
  .brand-dot { width: 18px; height: 18px; border-radius: 50%; background: var(--white); }
  .brand-name { font-weight: 700; font-size: 40px; color: var(--white); letter-spacing: -0.5px; }

  .title { position: absolute; left: 52px; top: 400px; }
  .title-main { font-family: "Oswald", Arial, sans-serif; font-weight: 600; font-size: 84px; line-height: 1; color: var(--orange); letter-spacing: 1px; }
  .title-sub { font-family: "Oswald", Arial, sans-serif; font-weight: 500; font-size: 38px; line-height: 1.1; color: var(--blue); letter-spacing: 1px; margin-top: 2px; }

  .tab { display: inline-block; background: var(--orange); color: var(--white); font-family: "Oswald", Arial, sans-serif; font-weight: 500; font-size: 20px; letter-spacing: 1px; padding: 2px 30px 2px 52px; clip-path: polygon(0 0, 100% 0, 92% 100%, 0 100%); }

  .about { position: absolute; left: 0; top: 590px; width: 515px; }
  .about p { padding: 10px 0 0 52px; font-size: 13.5px; line-height: 1.45; color: var(--muted); }
  .about p + p { padding-top: 8px; }
  .highlight { color: var(--orange); font-weight: 600; }

  .testimonials { position: absolute; left: 0; top: 880px; width: 515px; }
  .quote { padding: 10px 0 0 52px; font-size: 13.5px; line-height: 1.4; color: var(--ink); font-weight: 600; }
  .quote cite { display: block; font-style: italic; font-weight: 700; color: var(--ink); }

  .advantages { position: absolute; left: 548px; top: 400px; width: 252px; }
  .advantages-head { background: var(--orange); color: var(--white); font-family: "Oswald", Arial, sans-serif; font-weight: 500; font-size: 22px; letter-spacing: 1px; padding: 7px 18px; }
  .advantages-list { list-style: none; background: linear-gradient(180deg, var(--blue-mid), var(--blue)); padding: 16px 18px 18px 18px; }
  .advantages-list li { position: relative; padding-left: 24px; color: var(--white); font-size: 14px; line-height: 1.4; margin-bottom: 12px; }
  .advantages-list li:last-child { margin-bottom: 0; }
  .advantages-list li::before { content: ""; position: absolute; left: 2px; top: 7px; width: 8px; height: 8px; border-radius: 50%; background: var(--orange); }

  .skills { position: absolute; left: 548px; top: 916px; width: 252px; list-style: none; }
  .skills li { display: flex; align-items: center; gap: 14px; margin-bottom: 12px; font-size: 19px; font-weight: 600; color: var(--ink); }
  .skill-icon { width: 44px; height: 44px; flex: none; }

  .contact { position: absolute; left: 548px; top: 1090px; width: 252px; background: var(--blue); padding: 10px 16px; list-style: none; }
  .contact li { display: flex; align-items: center; gap: 10px; color: var(--white); font-size: 13.5px; font-weight: 600; line-height: 1.6; }
  .contact svg { width: 16px; height: 16px; flex: none; }

  .base-bar { position: absolute; left: 0; bottom: 0; width: 835px; height: 10px; background: var(--navy); }
</style>
</head>
<body>
<div class="flyer">

  <div class="hero">
    <div class="hero-photo" role="img" aria-label="Photo of a businessman in a suit touching glowing data graphics and a shopping trolley icon on a dark blue digital background"></div>
    <svg class="swoosh" viewBox="0 0 835 480" aria-hidden="true">
      <path d="M0 392 C 220 372, 420 290, 835 212 L 835 480 L 0 480 Z" fill="#ffffff"/>
      <path d="M0 384 C 220 364, 420 282, 835 204" fill="none" stroke="#f47b20" stroke-width="9"/>
      <path d="M0 372 C 220 352, 420 270, 835 192" fill="none" stroke="#ffffff" stroke-width="4" opacity="0.8"/>
    </svg>
    <div class="brand">
      <span class="brand-dot"></span>
      <span class="brand-name">Veltrane</span>
    </div>
  </div>

  <header class="title">
    <h1 class="title-main">WORKSHOPS</h1>
    <h2 class="title-sub">FOR DATA ANALYSTS</h2>
  </header>

  <section class="about">
    <h3 class="tab">ABOUT WORKSHOP</h3>
    <p>Our workshops have been attended by many of the UK's largest organisations and many international organisations too including Larkfield, Northbank, Petrona and XXX. Our workshops are run by experienced professionals including Martin Calloway, Veltrane's founder and the facilitator for Veltrane's flagship workshop 'Turning Figures Into Real Gains' – a workshop that has been running for <span class="highlight">over 10 years and become an essential</span> 'cornerstone' development session for many of our regular clients' analysts.</p>
    <p>We aim for our workshops to be educational, interactive, practical and fun – we believe we deliver on this but don't just take our word for it, here are some comments from our clients.</p>
  </section>

  <section class="testimonials">
    <h3 class="tab">TESTIMONIALS</h3>
    <blockquote class="quote">"We took from the course a number of actionable learnings that we have put into practice and this has resulted in positive feedback and a happier more valued team. Recommend the course to new and experienced analysts alike."<cite>– Dan Wilder, Aidwell</cite></blockquote>
    <blockquote class="quote">"One of the best courses I have been on. Very intuitive and has given me clear strategies on analysis to take back to my workplace."<cite>– Ruth Ellery, Linecall</cite></blockquote>
  </section>

  <aside class="advantages">
    <h3 class="advantages-head">ADVANTAGES</h3>
    <ul class="advantages-list">
      <li>CPD accredited</li>
      <li>Unique</li>
      <li>99.4% of past attendees would recommend the workshop to other analysts</li>
      <li>Has plenty of positive testimonials</li>
      <li>Been attended by UK's largest organisations and regularly by some</li>
      <li>Been running for over 10 years</li>
      <li>Cornerstone workshop in the development of analysts</li>
    </ul>
  </aside>

  <ul class="skills">
    <li>
      <svg class="skill-icon" viewBox="0 0 44 44" aria-hidden="true"><circle cx="22" cy="22" r="21" fill="#1c5fa8"/><path d="M12 15h14v9h-8l-4 4v-4h-2z" fill="#fff"/><path d="M28 19h5v9h-2v3l-3-3h-6v-2h6z" fill="#fff"/></svg>
      Communication
    </li>
    <li>
      <svg class="skill-icon" viewBox="0 0 44 44" aria-hidden="true"><circle cx="22" cy="22" r="21" fill="#1c5fa8"/><rect x="13" y="14" width="18" height="17" rx="2" fill="#fff"/><rect x="13" y="14" width="18" height="4" fill="#f47b20"/><path d="M17 24l3 3 6-6" stroke="#1c5fa8" stroke-width="2" fill="none"/></svg>
      Planning
    </li>
    <li>
      <svg class="skill-icon" viewBox="0 0 44 44" aria-hidden="true"><circle cx="22" cy="22" r="21" fill="#1c5fa8"/><rect x="13" y="24" width="4" height="8" fill="#fff"/><rect x="20" y="18" width="4" height="14" fill="#fff"/><rect x="27" y="13" width="4" height="19" fill="#f47b20"/></svg>
      Presentation Of Data
    </li>
  </ul>

  <ul class="contact">
    <li><svg viewBox="0 0 16 16" aria-hidden="true"><circle cx="8" cy="8" r="8" fill="#f47b20"/><path d="M5 4l2 0 1 2-1 1c.5 1 1 1.5 2 2l1-1 2 1v2c-4 0-7-3-7-7z" fill="#fff"/></svg>0161 000 4827</li>
    <li><svg viewBox="0 0 16 16" aria-hidden="true"><circle cx="8" cy="8" r="8" fill="#f47b20"/><rect x="4" y="5" width="8" height="6" fill="#fff"/><path d="M4 5l4 3 4-3" stroke="#f47b20" fill="none"/></svg>info@veltranepartners.co.uk</li>
    <li><svg viewBox="0 0 16 16" aria-hidden="true"><circle cx="8" cy="8" r="8" fill="#f47b20"/><circle cx="8" cy="8" r="4" stroke="#fff" fill="none"/><path d="M4 8h8M8 4v8" stroke="#fff"/></svg>www.veltranepartners.co.uk</li>
  </ul>

  <div class="base-bar"></div>
</div>
</body>
</html>
```